CPA, Management and IT Consulting Redesign Existing Website

We currently have a website that is outdated (www.qelvarn.com). We need a good website developer that can redesign our website. To make this easier I have chosen a few websites that we like the layout or template. Use our exiting website content for this project. Our new logo is attached below. Based on who wins this we will upgrade to a coded website and a content management system (CMS) so we can make changes to the text ourselves in the future.

http://www.brontekhaile.com/
http://www.lorvicanmanagement.com/

Target Market(s)

Government Clients

Industry/Entity Type

Management Consulting

Number of Pages Required

5+ page

Font styles to use
Serif

Requirements
Must have
• Please the following website templates as a guide.
• http://www.brontekhaile.com/
• http://www.lorvicanmanagement.com/
Nice to have
Should not have

```html
<!DOCTYPE html>
<html lang="en">
<head>
<meta charset="utf-8">
<title>Corvane Enterprises, LLC</title>
<link href="https://fonts.googleapis.com/css2?family=Roboto+Slab:wght@400;700&family=Open+Sans:ital,wght@0,400;0,600;0,700;1,400;1,600&display=swap" rel="stylesheet">
<style>
:root{
  --orange:#f39433;
  --orange-dark:#e07f1f;
  --ink:#1f1f1f;
  --text:#555;
  --white:#fff;
  --grey-band:#eeeeee;
  --footer:#474747;
  --footer-bar:#353535;
  --footer-text:#d8d8d8;
}
*{margin:0;padding:0;box-sizing:border-box}
html,body{width:1200px;height:2436px;overflow:hidden}
body{position:relative;background:var(--white);font-family:"Open Sans",Arial,sans-serif;color:var(--text)}
.abs{position:absolute}

/* header */
.site-header{position:absolute;left:0;top:0;width:1200px;height:110px;background:var(--white)}
.brand{position:absolute;left:100px;top:26px;display:flex;align-items:center;gap:12px}
.brand-mark{width:56px;height:56px;background:var(--orange)}
.brand-name{font-family:"Roboto Slab",Georgia,serif;font-weight:700;font-size:28px;line-height:1;color:var(--ink);text-transform:uppercase}
.main-nav{position:absolute;top:48px;left:575px;display:flex;font-size:13px;text-transform:uppercase;color:var(--ink);font-weight:600}
.main-nav span{margin-right:40px}
.main-nav .is-active{color:var(--orange);font-weight:400}
.search-icon{position:absolute;left:1086px;top:48px}

/* hero */
.hero{position:absolute;left:0;top:110px;width:1200px;height:514px;background:linear-gradient(110deg,#e9e3df 0%,#cdbfb6 35%,#8c6a56 60%,#5a3a29 85%,#3e2a1f 100%)}
.hero-caption{position:absolute;left:598px;top:210px;width:378px;height:120px;background:rgba(40,40,40,.82);color:var(--white);font-family:"Roboto Slab",Georgia,serif;font-size:26px;line-height:40px;padding:20px 0 0 40px;text-transform:uppercase;white-space:nowrap}
.hero-arrow{position:absolute;top:256px;width:38px;height:38px;border:2px solid var(--white);border-radius:50%}

/* section titles */
.section-title{position:absolute;left:0;width:1200px;text-align:center;font-family:"Roboto Slab",Georgia,serif;font-weight:700;font-size:30px;text-transform:uppercase;color:var(--ink)}
.section-title em{font-style:normal;color:var(--orange)}

/* welcome */
.welcome-text{position:absolute;left:140px;top:722px;width:920px;text-align:center;font-size:12.4px;line-height:22px;color:var(--text)}
.btn-primary{position:absolute;left:538px;top:838px;width:124px;height:36px;background:var(--orange);color:var(--white);font-size:11.5px;text-transform:uppercase;text-align:center;line-height:36px;border-radius:2px;border-bottom:2px solid var(--orange-dark)}

/* services */
.services{position:absolute;left:0;top:929px;width:1200px;height:442px;background:linear-gradient(90deg,#141414,#2a2a2a 45%,#1a1a1a 100%)}
.service{position:absolute;top:124px;width:250px;text-align:center;color:var(--white)}
.service-badge{margin:0 auto;width:140px;height:140px;border-radius:50%;background:#3a3a3a;display:flex;align-items:center;justify-content:center}
.service-badge-inner{width:118px;height:118px;border-radius:50%;background:var(--orange);display:flex;align-items:center;justify-content:center}
.service h3{margin-top:26px;font-size:15px;font-weight:700;text-transform:uppercase;line-height:20px}
.service h3.one-line{white-space:nowrap}
.service p{margin:12px auto 0;width:220px;font-size:12.2px;line-height:20px;color:#e6e6e6}

/* testimonials */
.testimonial{position:absolute;top:1496px;width:420px}
.avatar{position:absolute;left:0;top:0;width:102px;height:102px;border-radius:50%;border:3px solid #e4e4e4;background:radial-gradient(circle at 50% 45%,#d8cfc6 0,#b9aca0 45%,#33394a 70%,#f1f1f1 71%)}
.quote{position:absolute;left:120px;top:4px;width:290px;font-size:12.2px;line-height:21px;text-align:justify;color:var(--text)}
.quote-mark{font-family:"Roboto Slab",Georgia,serif;font-size:22px;color:#555;margin-right:14px}
.author{position:absolute;left:120px;top:102px;font-size:12.2px;font-style:italic;font-weight:600;color:var(--ink);text-transform:uppercase}

/* industries */
.industries{position:absolute;left:0;top:1730px;width:1200px;height:345px;background:var(--grey-band)}
.industry{position:absolute;top:98px;width:240px;height:198px}
.industry-label{position:absolute;bottom:24px;left:26px;right:26px;background:var(--white);text-align:center;font-size:15px;font-weight:600;color:var(--ink);line-height:19px;padding:10px 0}

/* partners */
.partner{position:absolute;top:2108px;display:flex;align-items:center;gap:10px;font-weight:600;font-size:22px;color:#555}
.partner-dot{width:28px;height:28px;border-radius:50%;background:#555}

/* footer */
.site-footer{position:absolute;left:0;top:2176px;width:1200px;height:214px;background:var(--footer);color:var(--footer-text)}
.footer-col{position:absolute;top:34px}
.footer-col h4{font-size:15.5px;font-weight:600;color:var(--white);margin-bottom:18px}
.footer-list{list-style:none;font-size:12.4px;line-height:29px}
.footer-list li{display:flex;align-items:center;gap:12px}
.chev{color:var(--white);font-size:12px}
.field{width:176px;height:32px;border:1px solid #5e5e5e;background:#4c4c4c;font-size:10px;font-style:italic;color:#bbb;padding:9px 10px;margin-top:16px}
.btn-subscribe{width:92px;height:28px;background:var(--orange);color:var(--white);font-size:10.5px;font-weight:700;text-transform:uppercase;text-align:center;line-height:28px;border-radius:2px;margin-top:16px}
.social-dot{width:14px;height:14px;border-radius:50%;background:var(--white)}
.footer-bar{position:absolute;left:0;top:2390px;width:1200px;height:46px;background:var(--footer-bar);color:var(--footer-text);font-size:12px;line-height:46px}
.footer-bar .legal{position:absolute;left:100px}
.footer-bar .links{position:absolute;left:856px}
</style>
</head>
<body>

<header class="site-header">
  <div class="brand"><div class="brand-mark"></div><div class="brand-name">Corvane<br>Enterprises, LLC</div></div>
  <nav class="main-nav">
    <span class="is-active">Home</span><span>About Us</span><span>Services</span><span>Industries</span><span>Contact Us</span>
  </nav>
  <svg class="search-icon" width="16" height="16" viewBox="0 0 16 16"><circle cx="6.5" cy="6.5" r="4.8" fill="none" stroke="#1f1f1f" stroke-width="2.2"/><line x1="10" y1="10" x2="14.5" y2="14.5" stroke="#1f1f1f" stroke-width="2.6" stroke-linecap="round"/></svg>
</header>

<section class="hero" role="img" aria-label="Close-up of a hand pointing at a printed bar chart beside a laptop on a wooden desk">
  <div class="hero-caption">Complex Challenges<br>Delivered Solutions</div>
  <div class="hero-arrow" style="left:30px"><svg width="34" height="34" viewBox="0 0 34 34"><polyline points="19,12 14,17 19,22" fill="none" stroke="#fff" stroke-width="2"/></svg></div>
  <div class="hero-arrow" style="left:1132px"><svg width="34" height="34" viewBox="0 0 34 34"><polyline points="15,12 20,17 15,22" fill="none" stroke="#fff" stroke-width="2"/></svg></div>
</section>

<h2 class="section-title" style="top:670px">Welcome <em>Corvane Enterprises, LLC</em></h2>
<p class="welcome-text">Corvane enterprises, LLC and Ashby &amp; Merrow, LLC is a network of certified public accounting and management consulting firms with seasoned professionals and an excellent reputation for serving a diverse client base including federal agencies, state and local government, non-profit organizations, small and medium-sized business entities, professional associations and individuals. We are committed to professional excellence across all service areas including Audit and Assurance, Accounting, Tax, Management Consulting, and Information Technology. Find out more.</p>
<div class="btn-primary">Find out more</div>

<section class="services">
  <h2 class="section-title" style="top:38px;color:var(--white)">Services <em>and Solutions</em></h2>
  <div class="service" style="left:89px">
    <div class="service-badge"><div class="service-badge-inner">
      <svg width="44" height="44" viewBox="0 0 44 44"><path d="M10 6h18l6 6v26H10z" fill="#fff"/><line x1="15" y1="16" x2="26" y2="16" stroke="#f39433" stroke-width="2"/><line x1="15" y1="21" x2="24" y2="21" stroke="#f39433" stroke-width="2"/><circle cx="27" cy="30" r="6" fill="#f39433" stroke="#fff" stroke-width="2"/><line x1="24" y1="33" x2="30" y2="27" stroke="#fff" stroke-width="1.5"/></svg>
    </div></div>
    <h3 class="one-line">Audit, Accounting and Tax</h3>
    <p>We offer a full range of assurance services that translates numbers into accurate, meaningful information for quality decision-making.</p>
  </div>
  <div class="service" style="left:350px">
    <div class="service-badge"><div class="service-badge-inner">
      <svg width="48" height="48" viewBox="0 0 48 48"><circle cx="20" cy="14" r="7" fill="#fff"/><path d="M7 38c0-9 6-14 13-14s11 4 12 9v5z" fill="#fff"/><circle cx="34" cy="33" r="8" fill="#f39433" stroke="#fff" stroke-width="2.5"/><text x="34" y="37.5" font-size="12" font-family="Open Sans,sans-serif" font-weight="700" fill="#fff" text-anchor="middle">$</text></svg>
    </div></div>
    <h3 class="one-line">Financial Management</h3>
    <p>We offer a full range of assurance services that translates numbers into accurate, meaningful information for quality decision-making.</p>
  </div>
  <div class="service" style="left:610px">
    <div class="service-badge"><div class="service-badge-inner">
      <svg width="48" height="48" viewBox="0 0 48 48"><rect x="6" y="8" width="36" height="24" rx="2" fill="none" stroke="#fff" stroke-width="3"/><rect x="15" y="14" width="5" height="4" fill="#fff"/><rect x="22" y="14" width="5" height="4" fill="#fff"/><rect x="29" y="14" width="5" height="4" fill="#fff"/><rect x="15" y="21" width="5" height="4" fill="#fff"/><rect x="22" y="21" width="5" height="4" fill="#fff"/><rect x="21" y="32" width="6" height="6" fill="#fff"/><rect x="14" y="38" width="20" height="3" fill="#fff"/></svg>
    </div></div>
    <h3 class="one-line">Information Technology</h3>
    <p>We offer a full range of assurance services that translates numbers into accurate, meaningful information for quality decision-making.</p>
  </div>
  <div class="service" style="left:871px">
    <div class="service-badge"><div class="service-badge-inner">
      <svg width="48" height="48" viewBox="0 0 48 48"><path d="M24 5l4 6h-8z" fill="#fff"/><path d="M14 18a10 7 0 0 1 20 0z" fill="#fff"/><rect x="10" y="19" width="28" height="3" fill="#fff"/><rect x="12" y="24" width="3" height="12" fill="#fff"/><rect x="18" y="24" width="3" height="12" fill="#fff"/><rect x="27" y="24" width="3" height="12" fill="#fff"/><rect x="33" y="24" width="3" height="12" fill="#fff"/><rect x="8" y="38" width="32" height="4" fill="#fff"/></svg>
    </div></div>
    <h3>Governance,Risk and<br>Compliance</h3>
    <p>We offer a full range of assurance services that translates numbers into accurate, meaningful information for quality decision-making.</p>
  </div>
</section>

<h2 class="section-title" style="top:1424px">Our <em>Testimonials</em></h2>
<div class="testimonial" style="left:171px">
  <div class="avatar" role="img" aria-label="Portrait of a client in a dark suit"></div>
  <p class="quote"><span class="quote-mark">&#8220;</span>Lorem ipsum dolor sit amet, consectetur adipiscing elit, sed do eiusmod tempor incididunt ut labore et dolore magna aliqua. Ut enim ad minim</p>
  <div class="author">John Doe</div>
</div>
<div class="testimonial" style="left:614px">
  <div class="avatar" role="img" aria-label="Portrait of a client in a grey suit"></div>
  <p class="quote"><span class="quote-mark">&#8220;</span>Lorem ipsum dolor sit amet, consectetur adipiscing elit, sed do eiusmod tempor incididunt ut labore et dolore magna aliqua. Ut enim ad minim</p>
  <div class="author">Doe John</div>
</div>
<svg class="abs" style="left:556px;top:1637px" width="90" height="38" viewBox="0 0 90 38">
  <circle cx="18" cy="19" r="16" fill="none" stroke="#d0d0d0" stroke-width="2"/><polyline points="21,12 14,19 21,26" fill="none" stroke="#c4c4c4" stroke-width="2.5"/>
  <circle cx="69" cy="19" r="16" fill="none" stroke="#d0d0d0" stroke-width="2"/><polyline points="66,12 73,19 66,26" fill="none" stroke="#c4c4c4" stroke-width="2.5"/>
</svg>

<section class="industries">
  <h2 class="section-title" style="top:32px">Our <em>Industries</em></h2>
  <div class="industry" style="left:100px;background:linear-gradient(160deg,#cfe2ee,#5d87a6 55%,#1f3f5c)" role="img" aria-label="Classical stone columns against a blue sky">
    <div class="industry-label">Federal Government</div></div>
  <div class="industry" style="left:352px;background:linear-gradient(180deg,#8aa6c4,#c7d2dc 50%,#6e6e6e)" role="img" aria-label="Capitol dome under a cloudy sky">
    <div class="industry-label">State and<br>Local Government</div></div>
  <div class="industry" style="left:600px;background:linear-gradient(180deg,#e9ecef,#b9c2c9 55%,#3a3a3a)" role="img" aria-label="Business team at a presentation board">
    <div class="industry-label">Financial Services</div></div>
  <div class="industry" style="left:861px;background:linear-gradient(180deg,#7d96ad,#d8b888 60%,#1a1a1a)" role="img" aria-label="Crowd silhouette at sunset lifting a person">
    <div class="industry-label">Not-for-Profit</div></div>
</section>

<div class="partner" style="left:110px"><div class="partner-dot"></div>Quillbase</div>
<div class="partner" style="left:326px"><div class="partner-dot"></div>Tessaro</div>
<div class="partner" style="left:538px"><div class="partner-dot"></div>Velmont</div>
<div class="partner" style="left:746px"><div class="partner-dot"></div>Brindle</div>
<div class="partner" style="left:958px"><div class="partner-dot"></div>Ostrix</div>

<footer class="site-footer">
  <div class="footer-col" style="left:114px">
    <h4>Contact Us</h4>
    <ul class="footer-list" style="line-height:24px">
      <li><svg width="10" height="14" viewBox="0 0 10 14"><path d="M5 0a5 5 0 0 1 5 5c0 4-5 9-5 9S0 9 0 5a5 5 0 0 1 5-5z" fill="#f39433"/><circle cx="5" cy="5" r="2" fill="#474747"/></svg><span style="margin-left:8px">4417 Marlow Street NW, Suite 300</span></li>
      <li style="padding-left:30px">Washington, DC 20006</li>
      <li style="margin-top:10px"><svg width="16" height="16" viewBox="0 0 16 16"><path d="M3 1l3 3-2 2c1 2 3 4 5 5l2-2 3 3-2 3C7 14 2 9 1 3z" fill="none" stroke="#f39433" stroke-width="1.4"/></svg><span style="margin-left:4px">(202) 555-0148</span></li>
      <li style="margin-top:10px"><svg width="18" height="12" viewBox="0 0 18 12"><rect x="1" y="1" width="16" height="10" fill="none" stroke="#f39433" stroke-width="1.4"/><polyline points="1,1 9,7 17,1" fill="none" stroke="#f39433" stroke-width="1.4"/></svg><span style="margin-left:2px">info@qelvarn.com</span></li>
    </ul>
  </div>
  <div class="footer-col" style="left:403px">
    <h4>Industries</h4>
    <ul class="footer-list">
      <li><span class="chev">&#187;</span>Federal Government</li>
      <li><span class="chev">&#187;</span>State and Local Government</li>
      <li><span class="chev">&#187;</span>Financial Services</li>
      <li><span class="chev">&#187;</span>Not-For-Profit</li>
    </ul>
  </div>
  <div class="footer-col" style="left:705px">
    <h4>Newsletter sign up</h4>
    <div style="font-size:12.4px">Please sign up here for &nbsp;news</div>
    <div class="field">Email address</div>
    <div class="btn-subscribe">Subscribe</div>
  </div>
  <div class="footer-col" style="left:990px">
    <h4>Follow Us</h4>
    <ul class="footer-list">
      <li><span class="social-dot"></span>Friendlane</li>
      <li><span class="social-dot"></span>Chirpwell</li>
      <li><span class="social-dot"></span>Circlenet</li>
    </ul>
  </div>
</footer>
<div class="footer-bar">
  <span class="legal">&copy; 2016 Corvane Enterprises All right reserved &nbsp;Term of Use</span>
  <span class="links">Testimonia &nbsp;&nbsp;| &nbsp;&nbsp;About Us &nbsp;&nbsp;| &nbsp;&nbsp;Blog &nbsp;&nbsp;| &nbsp;&nbsp;Contact</span>
</div>

</body>
</html>
```